A label for my commercially sold local honey. This is a LABEL not a logo

3 inches high
2 inches wide

Target Market(s)

Customers who like "local" honey

Logo Text

Wildflower Honey -- 100% Pure & Unfiltered -- Florida

Logo styles of interest
Wordmark Logo
Requirements
Must have
• Wildflower Honey -- 100% Pure & Unfiltered -- Florida

Florida should be dominant

3 inches high / 2 inches wide

```html
<!DOCTYPE html>
<html lang="en">
<head>
<meta charset="UTF-8">
<title>Wildflower Honey Label</title>
<link href="https://fonts.googleapis.com/css2?family=Archivo+Black&family=Delius&family=Stint+Ultra+Condensed&display=swap" rel="stylesheet">
<style>
  :root {
    --backdrop: #fde58a;
    --label-white: #ffffff;
    --honey-gold: #f9ae42;
    --amber-text: #d6884a;
  }
  html, body {
    margin: 0;
    padding: 0;
    width: 1200px;
    height: 1200px;
    overflow: hidden;
    background: var(--backdrop);
  }
  .canvas {
    position: relative;
    width: 1200px;
    height: 1200px;
    background: var(--backdrop);
  }
  .label {
    position: absolute;
    left: 280px;
    top: 113px;
    width: 640px;
    height: 974px;
  }
  .label-shape {
    position: absolute;
    inset: 0;
    width: 640px;
    height: 974px;
  }
  .label-text {
    position: absolute;
    left: 0;
    width: 640px;
    text-align: center;
    color: var(--amber-text);
    margin: 0;
  }
  .product-name {
    font-family: "Stint Ultra Condensed", serif;
    font-size: 150px;
    line-height: 1;
    letter-spacing: 3px;
  }
  .product-name.line-one { top: 232px; }
  .product-name.line-two { top: 372px; }
  .maker-name {
    top: 540px;
    font-family: "Stint Ultra Condensed", serif;
    font-size: 64px;
    line-height: 1;
    letter-spacing: 2px;
  }
  .tagline {
    top: 660px;
    font-family: "Delius", sans-serif;
    font-size: 21px;
    letter-spacing: 3px;
  }
  .origin {
    top: 712px;
    font-family: "Archivo Black", sans-serif;
    font-size: 80px;
    line-height: 1;
    letter-spacing: 1px;
  }
</style>
</head>
<body>
<main class="canvas">
  <section class="label">
    <svg class="label-shape" viewBox="0 0 920 1400" xmlns="http://www.w3.org/2000/svg">
      <path class="label-body" fill="var(--label-white)"
        d="M0 150 C0 90 25 40 50 0 L870 0 C895 40 920 90 920 150 L920 1100 C920 1130 905 1150 880 1165 L500 1385 C475 1398 445 1398 420 1385 L40 1165 C15 1150 0 1130 0 1100 Z"/>
      <path class="label-frame" fill="none" stroke="var(--honey-gold)" stroke-width="8"
        d="M28 150 L28 1095 C28 1115 38 1128 55 1137 L440 1325 C452 1331 468 1331 480 1325 L865 1137 C882 1128 892 1115 892 1095 L892 150"/>
      <path class="honeycomb-band" role="img" aria-label="Honeycomb pattern of golden hexagons across the top of the label"
        fill="var(--honey-gold)"
        d="M0 150 C0 90 25 40 50 0 L870 0 C895 40 920 90 920 150 Z"/>
    </svg>
    <h1 class="label-text product-name line-one">Wildflower</h1>
    <p class="label-text product-name line-two">Honey</p>
    <p class="label-text maker-name">Sunhive Mkt.</p>
    <p class="label-text tagline">100% Pure &amp; Unfiltered</p>
    <p class="label-text origin">FLORIDA</p>
  </section>
</main>
</body>
</html>
```